Postcard Design

New Integrated low voltage company in Merritt island florida Called Coastline Signal Partners we offer Integrated Technology for Fire Alarm, Security Systems Access Control Systems CCTV Systems Audio/Video Systems Lighting Control Automation Voice/Data and 24 hour Monitoring Services
Industry/Entity Type
It Company

```html
<!DOCTYPE html>
<html lang="en">
<head>
<meta charset="utf-8">
<title>Coastline Signal Partners – Postcard</title>
<link href="https://fonts.googleapis.com/css2?family=Cinzel:wght@500&family=Open+Sans:wght@600;700;800&family=Great+Vibes&display=swap" rel="stylesheet">
<style>
  :root{
    --black:#050505;
    --navy:#0d1f52;
    --blue:#1d3f8f;
    --sky:#6fa8dc;
    --white:#ffffff;
    --gray-band:#9a9a9a;
    --sheet-gray:#ececec;
    --rule-pink:#f2c6cf;
    --script-red:#c0282e;
    --bullet-red:#d12b2b;
  }
  *{margin:0;padding:0;box-sizing:border-box}
  html,body{width:738px;height:1200px;overflow:hidden;background:var(--white)}
  body{position:relative;font-family:"Open Sans",Arial,sans-serif;color:var(--white)}
  .abs{position:absolute}

  /* Front */
  .front{left:0;top:0;width:738px;height:570px;background:var(--black);overflow:hidden}
  .front-band{left:0;top:0;width:738px;height:58px;
    background:linear-gradient(90deg,var(--navy),var(--blue) 55%,#3a67c4);
    border-bottom:2px solid #8fb4ec;z-index:2}
  .front-band h1{position:absolute;right:28px;top:11px;font-family:"Cinzel",serif;font-weight:500;
    font-size:30px;letter-spacing:1px;white-space:nowrap}
  .brand-dot{left:48px;top:118px;width:34px;height:34px;border-radius:50%;background:var(--blue)}
  .brand-name{left:94px;top:98px;font-weight:800;font-size:58px;line-height:1;color:var(--white)}
  .headline{left:275px;top:100px;width:290px;text-align:center;font-weight:800;font-size:31px;line-height:1.25}
  .handset{left:585px;top:115px;width:170px;height:330px;border-radius:26px;
    background:linear-gradient(160deg,#f4f4f4,#cfd3da 60%,#9aa3b0);transform:rotate(14deg)}
  .pitch{left:50px;top:258px;width:400px;text-align:center;font-weight:700;font-size:23px;line-height:1.3}
  .phone-line{left:50px;top:350px;width:400px;text-align:center;font-weight:800;font-size:34px;line-height:1.2}
  .service-strip{left:0;top:405px;width:738px;height:150px;background:linear-gradient(#b5b5b5,var(--gray-band));z-index:2}
  .tile{top:413px;width:160px;height:106px;border:2px solid var(--white);z-index:3}
  .tile.cams{left:32px;background:linear-gradient(135deg,#e9e9e9,#6b6b6b)}
  .tile.light{left:202px;background:linear-gradient(160deg,#2a4a8a,#c98a3c)}
  .tile.fire{left:381px;background:linear-gradient(135deg,#8d1414,#e23a2a)}
  .tile.alarm{left:547px;background:linear-gradient(135deg,#f2efe6,#b9b4a6)}
  .caption{top:530px;width:160px;text-align:center;font-weight:700;font-size:13px;z-index:3}

  /* Back */
  .back{left:0;top:642px;width:566px;height:475px;background:linear-gradient(180deg,#1b3d8a,var(--navy));border-right:1px solid var(--rule-pink)}
  .banner{left:0;top:650px;width:368px;height:146px;background:linear-gradient(120deg,#1c2a48,#6b4a2a 60%,#2c3d66)}
  .banner-name{left:22px;top:680px;font-weight:800;font-size:58px;line-height:1;color:var(--white)}
  .area-box{left:372px;top:650px;width:194px;height:146px;background:var(--white);border:1px solid var(--rule-pink);
    display:flex;align-items:center;justify-content:center;text-align:center;
    font-family:"Great Vibes",cursive;color:var(--script-red);font-size:30px;line-height:1.1}
  .right-blank{left:372px;top:803px;width:194px;height:314px;background:var(--white);border:1px solid var(--rule-pink)}
  .services{left:22px;top:808px;width:334px;height:240px;border-radius:8px;
    background:linear-gradient(180deg,#7fa9dc,#4a77bd);border:1px solid #a8c4ea}
  .services p{position:absolute;left:0;top:12px;width:334px;text-align:center;font-weight:800;font-size:17px;line-height:1.25}
  .services ul{position:absolute;left:0;top:80px;width:334px;list-style:none;text-align:center;font-weight:800;font-size:15.5px;line-height:1.28}
  .services li{position:relative}
  .services li::before{content:"";position:absolute;left:22px;top:6px;border-left:9px solid var(--bullet-red);
    border-top:5px solid transparent;border-bottom:5px solid transparent}
  .contact{left:22px;top:1058px;width:334px;text-align:center;font-weight:700;font-size:16px;line-height:1.4}
  .sheet-foot{left:0;top:1123px;width:738px;height:77px;background:var(--sheet-gray)}
  .sheet-foot-rule{left:90px;top:1123px;width:1px;height:77px;background:var(--rule-pink)}
</style>
</head>
<body>
  <section class="front abs">
    <div class="front-band abs"><h1>Coastline Signal Partners</h1></div>
    <div class="brand-dot abs"></div>
    <div class="brand-name abs">CSP</div>
    <div class="headline abs">For all of your<br>Fire and Security<br>needs!</div>
    <div class="handset abs" role="img" aria-label="Smartphone showing a security event notification"></div>
    <div class="pitch abs">Seamless integration with your<br>smart devices and 24 hour<br>monitoring.</div>
    <div class="phone-line abs">321-555-0142</div>
    <div class="service-strip abs"></div>
    <div class="tile cams abs" role="img" aria-label="Security camera kit photo"></div>
    <div class="tile light abs" role="img" aria-label="Landscape lighting at dusk photo"></div>
    <div class="tile fire abs" role="img" aria-label="Fire alarm panel and detector photo"></div>
    <div class="tile alarm abs" role="img" aria-label="Alarm system control panel photo"></div>
    <div class="caption abs" style="left:32px">Security Cameras</div>
    <div class="caption abs" style="left:202px">Lighting</div>
    <div class="caption abs" style="left:381px">Fire Alarms</div>
    <div class="caption abs" style="left:547px">Alarm Systems</div>
  </section>

  <div class="back abs"></div>
  <div class="banner abs" role="img" aria-label="Restaurant bar interior with screens photo"></div>
  <div class="banner-name abs">CSP</div>
  <div class="area-box abs">Servicing<br>Merritt Island<br>Florida<br>and Area</div>
  <div class="right-blank abs"></div>
  <div class="services abs">
    <p>We specialize in low voltage<br>systems to keep your home<br>and business SAFE.</p>
    <ul>
      <li>Fire Alarm</li>
      <li>Security Systems</li>
      <li>Access Control Systems</li>
      <li>CCTV Systems</li>
      <li>Audio/Video Systems</li>
      <li>Lighting Control Automation</li>
      <li>Voice/Data</li>
      <li>24 hour Monitoring Services</li>
    </ul>
  </div>
  <div class="contact abs">321-555-0142<br>hello@coastlinesignal.biz</div>
  <div class="sheet-foot abs"></div>
  <div class="sheet-foot-rule abs"></div>
</body>
</html>
```